" Foco em atendimento humanizado e de serviços de alta qualidade. Residencial para terceira idade. Os idosos são moradores e têm todas as necessidades do dia-a-dia atendidas. Equipe 24h, acompanhamento médico, atividades de terapias diversas, todas as refeições inclusas e hotelaria completa. "

```html
<!DOCTYPE html>
<html lang="pt-BR">
<head>
<meta charset="utf-8">
<title>Assinatura de email – Florescer Residencial</title>
<link href="https://fonts.googleapis.com/css2?family=Mulish:wght@400;600;700&display=swap" rel="stylesheet">
<style>
  :root {
    --brown: #6e5248;
    --brown-soft: #8a7168;
    --pink: #e9a3bb;
    --card: #ffffff;
    --page: #f1efed;
    --divider: #d9cfcb;
  }
  * { margin: 0; padding: 0; box-sizing: border-box; }
  html, body {
    width: 1200px; height: 1200px; overflow: hidden;
    background: var(--page);
    font-family: "Mulish", sans-serif;
    color: var(--brown);
  }
  .signature {
    position: absolute;
    left: 100px; top: 455px;
    width: 1000px; height: 290px;
    background: var(--card);
    border: 3px solid var(--brown);
    border-radius: 10px;
    display: flex;
    align-items: center;
  }
  .brand {
    width: 390px;
    height: 100%;
    display: flex;
    flex-direction: column;
    align-items: center;
    justify-content: center;
    gap: 6px;
  }
  .brand-row { display: flex; align-items: center; gap: 14px; }
  .brand-dot { width: 30px; height: 30px; border-radius: 50%; background: var(--pink); }
  .brand-name { font-size: 46px; font-weight: 400; letter-spacing: 3px; color: var(--brown); }
  .brand-sub { font-size: 14px; letter-spacing: 7px; color: var(--brown); text-transform: uppercase; }
  .divider { width: 2px; height: 200px; background: var(--divider); }
  .person { padding-left: 48px; width: 290px; }
  .person-name { font-size: 21px; font-weight: 700; }
  .person-role { font-size: 16px; color: var(--brown-soft); margin-top: 4px; }
  .person-phones { margin-top: 26px; font-size: 18px; font-weight: 700; line-height: 1.35; }
  .contact { flex: 1; font-size: 17px; color: var(--brown-soft); }
  .contact-list { list-style: none; }
  .contact-item { display: flex; align-items: center; gap: 12px; margin-bottom: 8px; }
  .contact-icon { width: 22px; height: 22px; flex: none; }
  .contact-address { margin-top: 26px; line-height: 1.3; }
</style>
</head>
<body>
  <section class="signature">
    <div class="brand">
      <div class="brand-row">
        <span class="brand-dot"></span>
        <span class="brand-name">FLORESCER</span>
      </div>
      <span class="brand-sub">Residencial</span>
    </div>
    <div class="divider"></div>
    <div class="person">
      <p class="person-name">Nome/Sobrenome</p>
      <p class="person-role">Diretor Comercial</p>
      <p class="person-phones">(11) 90000-4821<br>(11) 90000-4821</p>
    </div>
    <div class="contact">
      <ul class="contact-list">
        <li class="contact-item">
          <svg class="contact-icon" viewBox="0 0 22 22"><circle cx="11" cy="11" r="11" fill="#6e5248"/><rect x="5.5" y="7" width="11" height="8" rx="1" fill="none" stroke="#fff" stroke-width="1.4"/><path d="M5.8 7.5 L11 11.5 L16.2 7.5" fill="none" stroke="#fff" stroke-width="1.4"/></svg>
          mail@florescer.com.br
        </li>
        <li class="contact-item">
          <svg class="contact-icon" viewBox="0 0 22 22"><circle cx="11" cy="11" r="11" fill="#6e5248"/><circle cx="11" cy="11" r="5.5" fill="none" stroke="#fff" stroke-width="1.3"/><ellipse cx="11" cy="11" rx="2.4" ry="5.5" fill="none" stroke="#fff" stroke-width="1.1"/><line x1="5.5" y1="11" x2="16.5" y2="11" stroke="#fff" stroke-width="1.1"/></svg>
          www.florescer.com.br
        </li>
        <li class="contact-item">
          <svg class="contact-icon" viewBox="0 0 22 22"><circle cx="11" cy="11" r="11" fill="#6e5248"/></svg>
          /florescer_residencial
        </li>
      </ul>
      <p class="contact-address">Rua das Acácias, 820 | Centro<br>Rio de Janeiro/RJ</p>
    </div>
  </section>
</body>
</html>
```